Business Card Design

We would like a business card that utilizes our current logo and keeps with the same feel - elegant and organic. Our farm isn't about mass production, it's about excellence, education, beautiful events and flowers - people, culture, and community.

Target Market(s)

Patrons to our farm who are interested in weddings, events, or our flowers and vegetables.

Contact Information for Business Card

Name, address, cell email (Rosalind Hepworth, 2718 Wintervale Rd, Longmont, CO 80517, cell 30.412.6387, email rosalind@wintervalefarm.example)

```html
<!DOCTYPE html>
<html lang="en">
<head>
<meta charset="utf-8">
<title>Wintervale Farm — Business Card</title>
<link rel="stylesheet" href="https://fonts.googleapis.com/css2?family=Montserrat:wght@400;500;700&display=swap">
<style>
  :root {
    --backdrop: #e4e3e4;
    --card-white: #ffffff;
    --sage: #6f8b71;
    --sage-deep: #5f7c62;
    --sage-light: #7f9a81;
    --copper: #b57a45;
    --ink-gray: #6b6b6b;
    --divider: #9a9a9a;
  }
  * { box-sizing: border-box; margin: 0; padding: 0; }
  html, body {
    width: 1200px; height: 801px; overflow: hidden;
    background: var(--backdrop);
    font-family: "Montserrat", sans-serif;
  }
  .canvas {
    position: relative; width: 1200px; height: 801px;
    display: flex; align-items: center; justify-content: center; gap: 40px;
  }
  .card {
    width: 525px; height: 300px; position: relative;
    box-shadow: 0 6px 18px rgba(0,0,0,0.12);
  }
  .card--front { background: var(--card-white); }
  .card--back {
    background: var(--sage);
    display: flex; align-items: center; justify-content: center;
  }
  .brand-name {
    position: absolute; left: 0; right: 0; top: 70px;
    text-align: center; color: var(--sage-deep);
    font-weight: 500; font-size: 30px; letter-spacing: 1px;
  }
  .details {
    position: absolute; left: 0; right: 0; top: 172px;
    display: flex; justify-content: center; align-items: stretch;
  }
  .person { text-align: right; padding-right: 20px; }
  .person__name {
    color: var(--sage-deep); font-weight: 700; font-size: 17px;
    text-transform: uppercase; letter-spacing: 0.5px; margin-bottom: 4px;
  }
  .person__address { color: var(--ink-gray); font-size: 13px; line-height: 1.45; }
  .rule { width: 1px; background: var(--divider); }
  .contact { list-style: none; padding-left: 20px; }
  .contact li {
    display: flex; align-items: center; gap: 7px;
    color: var(--ink-gray); font-size: 13px; line-height: 1.55;
  }
  .contact svg { width: 11px; height: 11px; fill: var(--copper); flex: none; }
  .pattern {
    position: absolute; inset: 0;
    background: linear-gradient(135deg, var(--sage-light), var(--sage) 55%, var(--sage-deep));
  }
  .back-brand {
    position: relative; color: var(--card-white);
    font-weight: 500; font-size: 24px; letter-spacing: 1px;
  }
</style>
</head>
<body>
<main class="canvas">
  <section class="card card--front" aria-label="Card front">
    <p class="brand-name">Wintervale Farm</p>
    <div class="details">
      <div class="person">
        <p class="person__name">Rosalind Hepworth</p>
        <p class="person__address">2718 Wintervale Rd<br>Longmont, CO 80517</p>
      </div>
      <div class="rule"></div>
      <ul class="contact">
        <li><svg viewBox="0 0 12 12"><path d="M3 1l2 2.5-1.2 1.3a7 7 0 003.4 3.4L8.5 7 11 9l-1.3 1.8C5.5 11 1 6.5 1.2 2.3z"/></svg>30.412.6387</li>
        <li><svg viewBox="0 0 12 12"><path d="M1 3h10v6H1z M1 3l5 3.5L11 3" stroke="#fff" stroke-width="0.8"/></svg>rosalind@wintervalefarm.example</li>
        <li><svg viewBox="0 0 12 12"><circle cx="6" cy="6" r="5"/><path d="M1 6h10M6 1c-2.5 3-2.5 7 0 10M6 1c2.5 3 2.5 7 0 10" stroke="#fff" stroke-width="0.7" fill="none"/></svg>www.wintervalefarm.example</li>
      </ul>
    </div>
  </section>
  <section class="card card--back" aria-label="Card back">
    <div class="pattern" role="img" aria-label="Tone-on-tone repeating brand-name pattern in sage green"></div>
    <p class="back-brand">Wintervale Farm</p>
  </section>
</main>
</body>
</html>
```